Front book cover for a training course to help bakers get higher prices and Win More Cake Orders.

We need a front cover for a book that will be teaching bakers how to sell wedding cakes to get higher prices and book more orders. It is a business book. Do not make it look like we want brides to read it. Bakers will be judging the cover to see if it is worth their investment to read it. The title is already in the logo, so do not repeat it.

Target Market(s)

Bakers who sell wedding cakes

Industry/Entity Type

Bakery

Colors

Designer to choose colors to be used in the design.

Requirements
Must have
• Must use the logo. Must have author name: Lou Brand. Must have subtitle: Boost Your Prices. Book More Brides. Build Your Empire.
Nice to have
• You are free to be creative. The concept is not to be pretty. It is a business sales and marketing book

```html
<!DOCTYPE html>
<html lang="en">
<head>
<meta charset="utf-8">
<title>Win More Cake Orders – Book Cover</title>
<link rel="stylesheet" href="https://fonts.googleapis.com/css2?family=Marcellus&family=Montserrat:wght@500&display=swap">
<style>
  :root {
    --page: #ffffff;
    --cover-pink: #ef5479;
    --accent-yellow: #f9b918;
    --accent-orange: #f29a1e;
    --ink-white: #ffffff;
    --ink-pink: #e9507a;
  }
  html, body {
    margin: 0;
    padding: 0;
    width: 1200px;
    height: 1200px;
    overflow: hidden;
    background: var(--page);
  }
  .canvas {
    position: relative;
    width: 1200px;
    height: 1200px;
    background: var(--page);
  }
  .book-cover {
    position: absolute;
    left: 222px;
    top: 31px;
    width: 762px;
    height: 1144px;
    background: var(--cover-pink);
  }
  .book-title {
    position: absolute;
    left: 0;
    right: 0;
    top: 82px;
    margin: 0;
    text-align: center;
    font-family: "Marcellus", serif;
    font-weight: 400;
    font-size: 124px;
    line-height: 116px;
    letter-spacing: 1px;
    color: var(--ink-white);
    -webkit-text-stroke: 1.5px var(--ink-white);
  }
  .book-title span { display: block; white-space: nowrap; }
  .author-band {
    position: absolute;
    left: 0;
    right: 0;
    top: 1047px;
    height: 77px;
    background: var(--accent-yellow);
    display: flex;
    align-items: center;
    justify-content: center;
  }
  .author-name {
    font-family: "Marcellus", serif;
    font-size: 60px;
    letter-spacing: 1px;
    color: var(--ink-pink);
    line-height: 1;
    padding-left: 10px;
  }
  .cover-art {
    position: absolute;
    left: 0;
    top: 0;
    width: 1200px;
    height: 1200px;
  }
  .bubble-fill { fill: var(--accent-yellow); }
  .bubble-shadow { fill: var(--accent-orange); }
  .bubble-outline { fill: none; stroke: var(--ink-white); stroke-width: 2.5; stroke-linejoin: miter; }
  .bubble-text {
    font-family: "Montserrat", sans-serif;
    font-weight: 500;
    font-size: 36px;
    fill: var(--ink-pink);
    text-anchor: middle;
    letter-spacing: -1px;
  }
  .brand-name {
    font-family: "Marcellus", serif;
    font-size: 54px;
    fill: var(--ink-white);
    text-anchor: middle;
  }
  .brand-dot { fill: none; stroke: var(--ink-white); stroke-width: 4; }
</style>
</head>
<body>
<main class="canvas">
  <section class="book-cover">
    <h1 class="book-title">
      <span>WIN MORE</span>
      <span>CAKE</span>
      <span>ORDERS</span>
    </h1>
    <div class="author-band">
      <span class="author-name">LOU BRAND</span>
    </div>
  </section>

  <svg class="cover-art" viewBox="0 0 1417 1417">
    <g class="bubble bubble-empire">
      <polygon class="bubble-shadow" points="328,682 568,716 556,840 520,840 500,866 484,834 350,810"/>
      <polygon class="bubble-fill" points="334,676 570,712 558,834 520,834 500,860 486,828 354,804"/>
      <polygon class="bubble-outline" points="337,669 575,716 560,840 522,838 500,866 482,835 355,806"/>
      <text class="bubble-text" transform="translate(456 735) rotate(8)">
        <tspan x="0" y="0">BUILD</tspan>
        <tspan x="0" y="34">YOUR</tspan>
        <tspan x="0" y="68">EMPIRE</tspan>
      </text>
    </g>

    <g class="bubble bubble-prices">
      <polygon class="bubble-shadow" points="840,712 1078,684 1064,810 928,836 906,866 890,840 852,842"/>
      <polygon class="bubble-fill" points="835,708 1072,680 1058,804 924,830 905,860 888,834 848,836"/>
      <polygon class="bubble-outline" points="831,714 1069,669 1050,808 924,834 905,864 885,838 846,840"/>
      <text class="bubble-text" transform="translate(944 730) rotate(-6)">
        <tspan x="0" y="0">BOOST</tspan>
        <tspan x="0" y="34">YOUR</tspan>
        <tspan x="0" y="68">PRICES</tspan>
      </text>
    </g>

    <g class="bubble bubble-brides">
      <polygon class="bubble-shadow" points="894,912 1132,878 1110,1016 988,1036 962,1068 946,1040 908,1040"/>
      <polygon class="bubble-fill" points="888,908 1126,874 1104,1010 984,1030 960,1062 944,1034 904,1034"/>
      <polygon class="bubble-outline" points="885,912 1124,868 1104,1006 980,1030 958,1066 940,1036 902,1040"/>
      <text class="bubble-text" transform="translate(998 932) rotate(-6)">
        <tspan x="0" y="0">BOOK</tspan>
        <tspan x="0" y="34">MORE</tspan>
        <tspan x="0" y="68">BRIDES</tspan>
      </text>
    </g>

    <g class="brand" role="img" aria-label="Layer Up Cakes brand name">
      <circle class="brand-dot" cx="700" cy="800" r="34"/>
      <text class="brand-name">
        <tspan x="700" y="915">Layer Up</tspan>
        <tspan x="700" y="985">Cakes</tspan>
      </text>
    </g>
  </svg>
</main>
</body>
</html>
```